Design us a professional website for a Cannabis Staffing Agency

We already have a logo ready to go, but now we are looking for a few good web designs. We provide staffing for the Cannabis/Marijuana industry. We want a good balance of clean, simple and modern design but also embracing the exciting atmosphere of the Cannabis industry.

Here are examples of our competition, please note that most of these competitors design feel old and dated:

http://qrvplacementcrew.example/
https://tolbrix.example/tolbrix-main-page
http://saffronpathways.example/index.html
http://www.wickcrew.example/medical-marijuana-staffing-recruiting
http://www.tundrahiring.example/
www.placedupcrew.example
www.pinewise.example

I also would prefer an explanation of why you choose to design it the way you did? What was your thought process or did you use a template?

Requirements
Must have
• About Us Page
• Candidates Page
• Employer Page
• Job Opening Page
• Contact Us Page
Nice to have
• Colors to match the logo, good use of images and design to show the story. Our goal is to show our clients what we are about and not just tell them.

```html
<!DOCTYPE html>
<html lang="en">
<head>
<meta charset="utf-8">
<title>Sprigwork – Contact</title>
<link rel="stylesheet" href="https://fonts.googleapis.com/css2?family=Gilda+Display&display=swap">
<style>
  :root {
    --leaf-green: #6a9a17;
    --ink: #111111;
    --paper: #ffffff;
    --footer-grey: #8e8e8e;
    --footer-rule: #3a3a3a;
    --map-land: #ece6d2;
    --map-water: #b9cbd8;
    --social-tile: #7b7b7b;
    --footer-dot: #6f6f6f;
  }
  * { margin: 0; padding: 0; box-sizing: border-box; }
  html, body { width: 1000px; height: 1200px; overflow: hidden; background: var(--paper); }
  body { position: relative; font-family: "Gilda Display", Georgia, serif; color: var(--ink); }

  .site-header {
    position: absolute; left: 0; top: 0; width: 1000px; height: 228px;
    background: var(--paper);
    box-shadow: 0 3px 3px rgba(0,0,0,0.55);
    z-index: 2;
  }
  .brand { position: absolute; display: flex; align-items: center; gap: 14px; }
  .brand-dot { width: 86px; height: 86px; border-radius: 50%; background: var(--leaf-green); flex: none; }
  .brand-name { font-size: 40px; color: var(--leaf-green); letter-spacing: 0.5px; line-height: 1; white-space: nowrap; }
  .site-header .brand { left: 30px; top: 42px; }

  .social { position: absolute; display: flex; gap: 11px; }
  .social-tile { width: 36px; height: 36px; border-radius: 6px; background: var(--leaf-green); }
  .site-header .social { left: 794px; top: 43px; }

  .main-nav { position: absolute; top: 180px; left: 0; width: 1000px; }
  .main-nav a {
    position: absolute; font-size: 24px; color: var(--ink); text-decoration: none; white-space: nowrap; line-height: 1;
  }
  .main-nav a.is-current { color: var(--leaf-green); }

  .contact-block { position: absolute; left: 49px; top: 284px; }
  .contact-title { font-size: 39px; color: var(--leaf-green); font-weight: 400; line-height: 1; }
  .contact-details { position: absolute; left: 57px; top: 70px; white-space: nowrap; }
  .contact-phone { font-size: 35px; line-height: 1; }
  .contact-place { font-size: 40px; line-height: 1; margin-top: 20px; }
  .contact-place + .contact-place { margin-top: 19px; }

  .location-map {
    position: absolute; left: 404px; top: 288px; width: 566px; height: 384px;
    border: 1px solid #9a9a9a;
    background: linear-gradient(100deg, var(--map-land) 0%, #efe8d4 58%, var(--map-water) 78%, #e9e3cd 100%);
  }

  .site-footer {
    position: absolute; left: 0; top: 833px; width: 1000px; height: 367px; background: var(--footer-grey); color: var(--paper);
  }
  .footer-rule { position: absolute; left: 467px; top: 73px; width: 2px; height: 227px; background: var(--footer-rule); }
  .footer-nav { position: absolute; left: 525px; top: 62px; list-style: none; }
  .footer-nav li { font-size: 23px; line-height: 42px; white-space: nowrap; }
  .footer-nav a { color: var(--paper); text-decoration: none; }
  .copyright { position: absolute; left: 30px; top: 192px; font-size: 22px; }
  .site-footer .brand { left: 24px; top: 248px; }
  .site-footer .brand-dot { background: var(--footer-dot); }
  .site-footer .social { left: 794px; top: 315px; }
  .site-footer .social-tile { background: var(--social-tile); }
</style>
</head>
<body>
  <header class="site-header">
    <div class="brand"><span class="brand-dot"></span><span class="brand-name">SPRIGWORK</span></div>
    <div class="social" aria-label="Social links">
      <span class="social-tile"></span><span class="social-tile"></span><span class="social-tile"></span><span class="social-tile"></span>
    </div>
    <nav class="main-nav">
      <a href="#" style="left:70px">HOME</a>
      <a href="#" style="left:167px">ABOUT US</a>
      <a href="#" style="left:310px">CANDIDATES</a>
      <a href="#" style="left:486px">EMPLOYERS</a>
      <a href="#" style="left:653px">JOB OPENING</a>
      <a href="#" class="is-current" style="left:834px">CONTACT</a>
    </nav>
  </header>

  <main>
    <section class="contact-block">
      <h1 class="contact-title">CONTACT</h1>
      <div class="contact-details">
        <p class="contact-phone">+915 0142 87</p>
        <p class="contact-place">ELM FIELD</p>
        <p class="contact-place">USA</p>
      </div>
    </section>
    <div class="location-map" role="img" aria-label="Road map of the upper Midwest with a highlighted route through Minnesota"></div>
  </main>

  <footer class="site-footer">
    <p class="copyright">copyright sprigwork.2017</p>
    <div class="brand"><span class="brand-dot"></span><span class="brand-name">SPRIGWORK</span></div>
    <div class="footer-rule"></div>
    <ul class="footer-nav">
      <li><a href="#">HOME</a></li>
      <li><a href="#">ABOUT US</a></li>
      <li><a href="#">CANDIDATES</a></li>
      <li><a href="#">EMPLOYERS</a></li>
      <li><a href="#">JOB OPENING</a></li>
      <li><a href="#">CONTACT</a></li>
    </ul>
    <div class="social" aria-label="Social links">
      <span class="social-tile"></span><span class="social-tile"></span><span class="social-tile"></span><span class="social-tile"></span>
    </div>
  </footer>
</body>
</html>
```